Brivora Distance Learning Website

Brivora provide e-learning and mixed learning solutions for individuals, colleges, organisations and B2B.
We need a modern, light and flat website design for Brivora. We want to to see the designer incorporate user experience(UX) design elements into the AI or PSD mockups. We would like to see designs that use pastel colors that compliment yellow and black of our logo.
We want our E-learning experience to accelerate learning and for the interface to be user friendly and intuitive. We want the designs to focus on quick access to course information, course reviews, learning progress and study advice. Quick and intuitive access to all content for our clients is one of our top priorities.
We would like designs for the following project 3 pages:
1. Learner homepage dashboard (see attached screenshot).
On this page the Learners need to:
- Login
- Have quick access to Packages and Courses.
- See other recommended courses (Below Packages and Courses)
- Possibly a left hand side column/menu with thumbnail icons (See lumivex learner dashboard screenshot)
2. Homepage
See current sample
http://www.brivora-learn.test
We would like the designer to focus on creating a customized banner to enhance the home page.
3. Primary Landing/Marketing page
This page is geared towards customer acquisition with the focal point being the top banner (video or HD image).
And Course Preview content below.
See reference
http://brivora-learn.test/subscriptionPlans/marketing/MTc%3D/Mjc4Nw%3D%3D/Quick%20Fennish%20%2B%20Fennish%20Nibbles%20Bundle%20by%20Harold%20Wen%20Pike
Other site we like:
- https://www.korvanta.test (We like the home page and top bar on courses page)
- http://www.tutorglen.test
- http://crewmapleden.test (think this site looks great, love the lower graphics on the homepage)
Updates
Hello,
Thank you for taking the time to contribute to this web design competition. We would just like to point out a few things:
1. Please try to make the color palette similar to the colors used in the screenshot that we just uploaded ('possible color palette).
2. Please make the designs specific to each page: THE LEARNER HOMEPAGE, HOME PAGE, and the MARKETING LANDING PAGE.
We are very happy with the high quality of designs so far,
Cheers,
Lee Ab
KV-Studio
Also,
Please avoid using dark/bold elements in the designs. The ONLY elements that we want to be dark are the logo and the footer.
Any questions please ask,
Cheers,
Lee Ab
Kv-Studio
Hello,
Based on the round of feedback we just gave it would be great if you could complete further design changes by tomorrow, as we are pushed for time.
Thank you,
Lee Ab
KV-Studio

```html
<!DOCTYPE html>
<html lang="en">
<head>
<meta charset="utf-8">
<title>Brivora – Learner Dashboard</title>
<link href="https://fonts.googleapis.com/css2?family=Open+Sans:wght@400;600;700&display=swap" rel="stylesheet">
<style>
:root{
  --yellow:#f6b81f;
  --yellow-soft:#fbe3a4;
  --ink:#222;
  --text:#444;
  --muted:#8a8a8a;
  --line:#e2e2e2;
  --panel:#f7f7f5;
  --link-blue:#2a5a9c;
  --footer:#262626;
  --white:#fff;
}
*{box-sizing:border-box;margin:0;padding:0}
html,body{width:1200px;height:2244px;overflow:hidden;background:var(--white);font-family:"Open Sans",Arial,sans-serif;color:var(--text)}
.page{position:relative;width:1200px;height:2244px}
.abs{position:absolute}

/* sidebar */
.side-nav{left:0;top:0;width:61px;height:614px;background:var(--yellow);display:flex;flex-direction:column;align-items:center;padding-top:22px}
.side-item{display:flex;flex-direction:column;align-items:center;text-align:center;font-size:8px;line-height:10px;color:var(--ink);width:61px;height:82px}
.side-item svg{width:24px;height:24px;margin-bottom:4px}

/* hero */
.hero{left:61px;top:0;width:1139px;height:614px;background:linear-gradient(100deg,#6f6a63 0%,#a9a59e 30%,#d9d8d4 55%,#eeeeec 80%,#c9c5bf 100%)}
.topbar{left:61px;top:0;width:1006px;height:72px;background:var(--white);display:flex;align-items:center;justify-content:space-between;padding:0 23px 0 84px}
.brand{display:flex;align-items:center;gap:8px;font-weight:700;font-size:26px;color:var(--ink)}
.brand-dot{width:26px;height:26px;border-radius:50%;background:var(--yellow)}
.top-links{display:flex;align-items:center;gap:28px;font-size:11px;color:#777;letter-spacing:.3px}
.top-links .active{color:var(--yellow)}
.top-links .login-btn{background:var(--yellow);color:var(--ink);padding:6px 10px}
.hero-title{left:157px;top:176px;font-size:47px;font-weight:700;line-height:47px;color:var(--white)}
.hero-btn{left:157px;top:284px;width:146px;height:39px;background:var(--yellow);color:var(--ink);font-size:15px;display:flex;align-items:center;justify-content:center;border-radius:2px}
.dots{left:561px;top:569px;width:76px;height:18px;border-radius:9px;background:rgba(60,60,60,.7);display:flex;align-items:center;justify-content:center;gap:7px}
.dots i{width:7px;height:7px;border-radius:50%;background:var(--white)}
.dots i.on{background:transparent;border:1.5px solid var(--white)}

/* login */
.login-box{left:147px;top:683px;width:400px;height:187px;border:1.5px solid var(--yellow);background:var(--panel);padding:20px 24px}
.login-box h2{font-size:28px;font-weight:600;color:var(--ink);display:flex;align-items:center;gap:10px;margin-bottom:14px}
.field{width:268px;height:37px;background:var(--white);border:1px solid var(--line);font-size:11px;color:#666;padding:0 16px;display:flex;align-items:center;margin-left:4px}
.login-row{display:flex;gap:8px;align-items:center;margin-top:13px}
.login-submit{width:70px;height:38px;background:var(--yellow);font-size:12px;color:var(--ink);display:flex;align-items:center;justify-content:center}
.welcome{left:572px;top:676px;width:480px}
.welcome h1{font-size:27px;font-weight:400;color:var(--yellow);margin-bottom:8px}
.welcome p{font-size:11px;line-height:19px;color:var(--muted)}
.search{left:572px;top:831px;width:382px;height:39px;background:#eaeaea;display:flex;align-items:center;justify-content:space-between;padding:0 14px 0 16px;font-size:11px;color:#555}

/* packages */
.packages{left:147px;top:923px;width:900px;height:574px;border:1.5px solid var(--yellow)}
.tabs{display:flex;height:51px;background:var(--yellow-soft);font-size:15px;color:var(--ink);white-space:nowrap}
.tab{display:flex;align-items:center;justify-content:center;height:51px}
.tab.active{background:var(--yellow);position:relative}
.tab.active::after{content:"";position:absolute;bottom:-9px;left:50%;margin-left:-9px;border:9px solid transparent;border-bottom:0;border-top-color:var(--yellow)}
.pkg{position:absolute;left:25px;width:845px;height:190px}
.pkg-img{position:absolute;left:0;top:0;width:189px;height:190px}
.pkg-body{position:absolute;left:211px;top:4px;width:625px}
.pkg-body h3{font-size:17px;font-weight:400;color:var(--ink);white-space:nowrap}
.pkg-by{font-size:11px;color:var(--muted);margin-top:3px;padding-bottom:12px;border-bottom:1px solid var(--line)}
.pkg-desc{font-size:11px;line-height:17px;color:var(--muted);margin-top:8px}
.chip{display:inline-block;background:#ececec;font-size:11px;color:#444;padding:7px 12px;margin-top:10px}
.meta{display:flex;margin-top:10px;font-size:11.5px;color:var(--ink);white-space:nowrap}
.meta small{display:block;font-size:9px;color:#555}
.meta .m-author{width:190px;border-right:1px solid #bbb}
.meta .m-code{width:135px;padding-left:30px;border-right:1px solid #bbb}
.meta .m-exp{padding-left:30px}

/* recommended */
.rec-head{left:147px;top:1540px;width:900px;display:flex;justify-content:space-between;align-items:center}
.rec-head h2{font-size:22px;font-weight:400;color:var(--yellow)}
.card{top:1580px;width:214px;height:278px;border:1px solid var(--line);background:var(--white)}
.card-img{height:133px}
.card-body{padding:14px 15px}
.card-body h4{font-size:11.5px;font-weight:400;line-height:17px;color:var(--ink)}
.card-body p{font-size:9.5px;line-height:14px;color:#777;margin-top:10px}
.more{font-size:9px;color:#777;margin-top:10px;display:flex;align-items:center;gap:3px}

/* quick links */
.links-band{left:0;top:1911px;width:1200px;height:206px;background:#f4f4f4}
.link-col{top:1934px;width:300px;display:flex;flex-wrap:wrap}
.link-col h5{width:100%;font-size:12px;font-weight:400;color:var(--link-blue);margin-bottom:8px}
.link-col ul{list-style:none;width:150px}
.link-col li{font-size:10px;line-height:21px;color:#777}
.link-col li::before{content:"• "}
.vsep{top:1940px;width:1px;height:140px;background:#ddd}

/* footer */
.footer{left:0;top:2117px;width:1200px;height:127px;background:var(--footer)}
.foot-brand{left:134px;top:2140px;width:123px;height:44px;background:#8d8d8d;display:flex;align-items:center;justify-content:center;gap:6px;font-weight:700;font-size:20px;color:var(--ink)}
.foot-div{left:410px;top:2117px;width:1px;height:127px;background:#3c3c3c}
.copy{left:134px;top:2203px;font-size:10px;color:#888}
.foot-nav{left:548px;top:2143px;font-size:10px;font-weight:600;color:#aaa;display:flex;gap:10px}
.foot-nav span.sep{color:#777;font-weight:400}
.foot-line{left:522px;top:2178px;width:544px;height:1px;background:#3c3c3c}
.social{left:880px;top:2197px;display:flex;gap:7px}
.social i{width:25px;height:25px;border-radius:50%;display:block}
.ver{left:1180px;top:2222px;font-size:9px;color:#888}
</style>
</head>
<body>
<div class="page">

  <div class="abs hero" role="img" aria-label="Photo of a young man in glasses studying at a laptop in a bright library"></div>

  <nav class="abs side-nav">
    <div class="side-item"><svg viewBox="0 0 24 24"><rect x="3" y="5" width="18" height="2.5" fill="#222"/><rect x="3" y="11" width="18" height="2.5" fill="#222"/><rect x="3" y="17" width="18" height="2.5" fill="#222"/></svg>Menu</div>
    <div class="side-item"><svg viewBox="0 0 24 24"><rect x="4" y="4" width="16" height="4" fill="#222"/><rect x="4" y="10" width="16" height="4" fill="#222"/><rect x="4" y="16" width="16" height="4" fill="#222"/></svg>Learning<br>Publishers<br>Dashboard</div>
    <div class="side-item"><svg viewBox="0 0 24 24"><rect x="3" y="8" width="18" height="12" rx="1" fill="#222"/><rect x="9" y="4" width="6" height="5" fill="none" stroke="#222" stroke-width="2"/></svg>Find<br>Learning<br>Packages</div>
    <div class="side-item"><svg viewBox="0 0 24 24"><polygon points="12,2 15,9 22,9.5 16.5,14 18.5,21 12,17 5.5,21 7.5,14 2,9.5 9,9" fill="#222"/></svg>Reviews &amp;<br>Comments</div>
    <div class="side-item"><svg viewBox="0 0 24 24"><path d="M6 3h13v15H8a2 2 0 0 0 0 3h11v1H8a3 3 0 0 1-3-3V4z" fill="#222"/></svg>Purchase<br>History</div>
    <div class="side-item"><svg viewBox="0 0 24 24"><circle cx="9" cy="10" r="6" fill="none" stroke="#222" stroke-width="3" stroke-dasharray="3 2"/><circle cx="17" cy="17" r="4" fill="none" stroke="#222" stroke-width="2.5" stroke-dasharray="2 1.5"/></svg>Settings</div>
    <div class="side-item"><svg viewBox="0 0 24 24"><path d="M12 3a6 6 0 0 1 6 6v6l2 3H4l2-3V9a6 6 0 0 1 6-6z" fill="#222"/><circle cx="12" cy="20" r="2" fill="#222"/></svg>Notifications</div>
  </nav>

  <header class="abs topbar">
    <div class="brand"><span class="brand-dot"></span>Brivora</div>
    <div class="top-links"><span class="active">PACKAGES</span><span>COURSES</span><span>TRIAL</span><span>REGISTER</span><span class="login-btn">LOGIN</span></div>
  </header>

  <div class="abs hero-title">Vestibulum<br>condimentum sem</div>
  <div class="abs hero-btn">Get Started Now</div>
  <div class="abs dots"><i class="on"></i><i></i><i></i><i></i></div>

  <section class="abs login-box">
    <h2><svg width="18" height="22" viewBox="0 0 18 22"><rect x="1" y="9" width="16" height="12" fill="#555"/><path d="M4 9V6a5 5 0 0 1 10 0" fill="none" stroke="#555" stroke-width="2.5"/></svg>Login</h2>
    <div class="field">E-mail</div>
    <div class="login-row"><div class="field">Password</div><div class="login-submit">LOGIN</div></div>
  </section>

  <section class="abs welcome">
    <h1>Welcome to Brivora</h1>
    <p>Aenean facilisis tincidunt lectus, id dictum nisi luctus eget. Vivamus efficitur ex condimentum, malesuada eros eget, feugiat nibh. Sed tellus ex, imperdiet eget gravida sit amet, volutpat eget turpis. In nec ultricies est. Etiam mattis augue vehicula odio posuere, sit amet tempus lectus luctus. Nulla facilisi. Etiam vel massa elementum, bibendum tellus venenatis, feugiat massa convallis molestie enim sit amet.</p>
  </section>
  <div class="abs search">Search Courses her...<svg width="18" height="18" viewBox="0 0 18 18"><circle cx="7.5" cy="7.5" r="5.5" fill="none" stroke="#444" stroke-width="2"/><line x1="11.5" y1="11.5" x2="16" y2="16" stroke="#444" stroke-width="2.5"/></svg></div>

  <section class="abs packages">
    <div class="tabs">
      <div class="tab" style="width:115px">Store</div>
      <div class="tab active" style="width:268px">Subscribed Learning Packages</div>
      <div class="tab" style="width:214px">My Published Packages</div>
      <div class="tab" style="width:145px">Bookmarks</div>
      <div class="tab" style="width:155px">My Rewards</div>
    </div>

    <article class="pkg" style="top:100px">
      <div class="pkg-img" role="img" aria-label="Bundle cover artwork with two letter symbols on a yellow and blue background" style="background:linear-gradient(180deg,#f3c623 0%,#f0b52b 55%,#e59a2a 100%)"></div>
      <div class="pkg-body">
        <h3>Quick Fennish + Fennish Nibbles Bundle by Harold Wen Pike</h3>
        <div class="pkg-by">Published BY - Harold Wen Pike Learning and Communication</div>
        <p class="pkg-desc">Fusce vitae lectus sit amet mi pulvinar maximus. Aenean placerat, nibh vel accumsan aliquet, magna nibh accumsan nibh, ac tempus nunc ipsum ac tellus. Cras augue magna, placerat eget nulla non, congue suscipit neque.</p>
        <span class="chip">Courses in Packages</span>
        <div class="meta">
          <div class="m-author"><small>Author</small>Fennish Nibbles by Harold Wen Pike</div>
          <div class="m-code"><small>Code</small>LEP - 000011</div>
          <div class="m-exp"><small>Product Expires</small>Never</div>
        </div>
      </div>
    </article>

    <article class="pkg" style="top:349px">
      <div class="pkg-img" role="img" aria-label="Illustration of hands holding a tablet with education icons on an orange background" style="background:linear-gradient(180deg,#f0573a,#e84a2e)"></div>
      <div class="pkg-body">
        <h3>Quick Fennish + Fennish Nibbles Bundle by Harold Wen Pike</h3>
        <div class="pkg-by">Published BY - Harold Wen Pike Learning and Communication</div>
        <p class="pkg-desc">Fusce vitae lectus sit amet mi pulvinar maximus. Aenean placerat, nibh vel accumsan aliquet, magna nibh accumsan nibh, ac tempus nunc ipsum ac tellus. Cras augue magna, placerat eget nulla non, congue suscipit neque.</p>
        <span class="chip">Courses in Packages</span>
        <div class="meta">
          <div class="m-author"><small>Author</small>Fennish Nibbles by Harold Wen Pike</div>
          <div class="m-code"><small>Code</small>LEP - 000011</div>
          <div class="m-exp"><small>Product Expires</small>Never</div>
        </div>
      </div>
    </article>
  </section>

  <div class="abs rec-head"><h2>Recommended Courses</h2><svg width="20" height="20" viewBox="0 0 20 20"><circle cx="10" cy="10" r="8.5" fill="none" stroke="#f6b81f" stroke-width="1.8"/><path d="M6 10h8M10.5 6.5 14 10l-3.5 3.5" fill="none" stroke="#f6b81f" stroke-width="1.8"/></svg></div>

  <article class="abs card" style="left:147px">
    <div class="card-img" role="img" aria-label="Photo of a woman working on a laptop" style="background:linear-gradient(135deg,#e9e4dc,#bdb6ac)"></div>
    <div class="card-body"><h4>Juisque aliquet ex nec est vestibu lum pulvinar</h4><p>Fusce vitae lectus sit amet mi pulvinar maximus. Aenean placerat, nibh vel accumsan aliquet, magna nibh.</p><div class="more">MORE <svg width="8" height="8"><circle cx="4" cy="4" r="3.3" fill="none" stroke="#999"/></svg></div></div>
  </article>
  <article class="abs card" style="left:376px">
    <div class="card-img" role="img" aria-label="Photo of a woman with a headset studying at a laptop" style="background:linear-gradient(135deg,#d9dde2,#a9b0b8)"></div>
    <div class="card-body"><h4>Juisque aliquet ex nec est vestibu lum pulvinar</h4><p>Fusce vitae lectus sit amet mi pulvinar maximus. Aenean placerat, nibh vel accumsan aliquet, magna nibh.</p><div class="more">MORE <svg width="8" height="8"><circle cx="4" cy="4" r="3.3" fill="none" stroke="#999"/></svg></div></div>
  </article>
  <article class="abs card" style="left:605px">
    <div class="card-img" role="img" aria-label="Illustration of colourful app icons rising from an open book" style="background:linear-gradient(180deg,#2f8fd8,#1b5fa8)"></div>
    <div class="card-body"><h4>Juisque aliquet ex nec est vestibu lum pulvinar</h4><p>Fusce vitae lectus sit amet mi pulvinar maximus. Aenean placerat, nibh vel accumsan aliquet, magna nibh.</p><div class="more">MORE <svg width="8" height="8"><circle cx="4" cy="4" r="3.3" fill="none" stroke="#999"/></svg></div></div>
  </article>
  <article class="abs card" style="left:834px">
    <div class="card-img" role="img" aria-label="Photo of a girl at a laptop with sketched icons around her" style="background:linear-gradient(135deg,#f4f4f2,#d5d5d2)"></div>
    <div class="card-body"><h4>Juisque aliquet ex nec est vestibu lum pulvinar</h4><p>Fusce vitae lectus sit amet mi pulvinar maximus. Aenean placerat, nibh vel accumsan aliquet, magna nibh.</p><div class="more">MORE <svg width="8" height="8"><circle cx="4" cy="4" r="3.3" fill="none" stroke="#999"/></svg></div></div>
  </article>

  <div class="abs links-band"></div>
  <div class="abs link-col" style="left:142px"><h5>Quick Links</h5>
    <ul><li>Integer lobortis</li><li>Curabitur ac</li><li>Phasellus tellus nisl</li><li>Aenean fringilla</li><li>Vestibulum</li><li>Aliquam commodo</li></ul>
    <ul><li>Integer lobortis</li><li>Curabitur ac</li><li>Phasellus tellus nisl</li><li>Aenean fringilla</li><li>Vestibulum</li><li>Aliquam commodo</li></ul></div>
  <div class="abs vsep" style="left:440px"></div>
  <div class="abs link-col" style="left:481px"><h5>Quick Links</h5>
    <ul><li>Integer lobortis</li><li>Curabitur ac</li><li>Phasellus tellus nisl</li><li>Aenean fringilla</li><li>Vestibulum</li><li>Aliquam commodo</li></ul>
    <ul><li>Integer lobortis</li><li>Curabitur ac</li><li>Phasellus tellus nisl</li><li>Aenean fringilla</li><li>Vestibulum</li><li>Aliquam commodo</li></ul></div>
  <div class="abs vsep" style="left:776px"></div>
  <div class="abs link-col" style="left:817px"><h5>Quick Links</h5>
    <ul><li>Integer lobortis</li><li>Curabitur ac</li><li>Phasellus tellus nisl</li><li>Aenean fringilla</li><li>Vestibulum</li><li>Aliquam commodo</li></ul>
    <ul><li>Integer lobortis</li><li>Curabitur ac</li><li>Phasellus tellus nisl</li><li>Aenean fringilla</li><li>Vestibulum</li><li>Aliquam commodo</li></ul></div>

  <footer class="abs footer"></footer>
  <div class="abs foot-brand"><span class="brand-dot" style="width:18px;height:18px"></span>Brivora</div>
  <div class="abs foot-div"></div>
  <div class="abs copy">Copyright © 2015 Brivora. All rights reserved.</div>
  <div class="abs foot-nav"><span>Home</span><span class="sep">|</span><span>Pages</span><span class="sep">|</span><span>Courses</span><span class="sep">|</span><span>Trial</span><span class="sep">|</span><span>Register</span><span class="sep">|</span><span>Login</span><span class="sep">|</span><span>Terms of Service</span><span class="sep">|</span><span>Privacy Policy</span></div>
  <div class="abs foot-line"></div>
  <div class="abs social"><i style="background:#3b5998"></i><i style="background:#2aa3e0"></i><i style="background:#555"></i><i style="background:#f25c22"></i><i style="background:#e52d27"></i><i style="background:#5aa646"></i></div>
  <div class="abs ver">M2</div>

</div>
</body>
</html>
```